Workvane Background Design

Need to develop a Workvane Background picture for my profile. The components I want in there are:
1) Name: Mohit Varma
2) Key Skills: Strategy, Innovation, Execution, Growth and Leadership
3) A photograph (an action photograph) The attached photograph is an example.
A black background would be ideal.

The design should meet the Workvane background size requirements.

The background should reinforce an image of a thinking person but equally capable of implementing.

Leadership

```html
<!DOCTYPE html>
<html lang="en">
<head>
<meta charset="utf-8">
<title>Mohit Varma – Workvane Background</title>
<link href="https://fonts.googleapis.com/css2?family=UnifrakturMaguntia&family=Cutive&display=swap" rel="stylesheet">
<style>
  :root {
    --bg: #000000;
    --ink: #ffffff;
    --overlay-bg: #ffffff;
    --overlay-text: #808080;
    --photo-top: #4a4a4a;
    --photo-mid: #3a3632;
    --photo-bottom: #8a7050;
  }
  html, body {
    margin: 0;
    padding: 0;
    overflow: hidden;
    background: var(--bg);
  }
  .banner {
    position: relative;
    width: 1200px;
    height: 364px;
    background: var(--bg);
    overflow: hidden;
  }
  .speaker-photo {
    position: absolute;
    left: 930px;
    top: 12px;
    width: 255px;
    height: 352px;
    background: linear-gradient(180deg, var(--photo-top) 0%, var(--photo-mid) 60%, var(--photo-bottom) 100%);
  }
  .name {
    position: absolute;
    right: 280px;
    top: 32px;
    margin: 0;
    font-family: "UnifrakturMaguntia", serif;
    font-weight: 400;
    font-size: 76px;
    line-height: 1;
    color: var(--ink);
    white-space: nowrap;
  }
  .skills {
    position: absolute;
    left: 159px;
    top: 129px;
    margin: 0;
    font-family: "Cutive", serif;
    font-size: 20.5px;
    line-height: 1.2;
    letter-spacing: 1.6px;
    color: var(--ink);
    white-space: nowrap;
  }
  .profile-overlay {
    position: absolute;
    left: 159px;
    top: 160px;
    width: 879px;
    height: 204px;
    background: var(--overlay-bg);
    display: flex;
    align-items: center;
    justify-content: center;
    padding-top: 10px;
    box-sizing: border-box;
  }
  .profile-overlay-label {
    font-family: Arial, Helvetica, sans-serif;
    font-size: 16px;
    color: var(--overlay-text);
  }
</style>
</head>
<body>
  <div class="banner">
    <div class="speaker-photo" role="img" aria-label="Action photograph of the speaker at a wooden podium, raising one finger"></div>

    <h1 class="name">Mohit Varma</h1>
    <p class="skills">Strategy, Innovation, Execution, Growth, and Leadership</p>

    <div class="profile-overlay">
      <span class="profile-overlay-label">{Workvane Profile overlay}</span>
    </div>
  </div>
</body>
</html>
```